Need a Crisps (Potato Chips in US) and Popcorns Logo, Artwork and Packaging Design

I want to package my home made crisps and popcorns. The crisps will be going by the name ZapZop (Ks are capital) and the popcorns by the name munbuns (Should all be in same case, either all small or all caps - I leave it to designer's choice).

Crisps:
I want both a logo that will be associated with the product and a package design with the logo embedded. The logo should be playful and striking.

The packaging for the crisps should be to the standards of international brands like Tavo, Wumbles, Flindas, etc. Package type is the pouch based packages.

The colours should be vibrant. We are limited to 4 colours in the design due to printing costs. So the designer should use a mixture that is striking especially to children and young adults.

Incorporation of animal artwork is allowed as long as it does not infringe on IPs.

Popcorns:
This one is less intensive and only requires a logo and package design like the one used in movie halls.

Target Market(s)

Kids and young adults

Industry/Entity Type

Food Production

Logo Text

ZapZop for crisps and munbuns for popcorn

Colors

Designer to choose colors to be used in the design.

Requirements
Must have
• Playful font and colours
Nice to have
• Distinguishing artwork

```html
<!DOCTYPE html>
<html lang="en">
<head>
<meta charset="utf-8">
<title>ZapZop Crisp Pouch</title>
<link rel="stylesheet" href="https://fonts.googleapis.com/css2?family=Lilita+One&family=Audiowide&family=Roboto:wght@500&display=swap">
<style>
  :root {
    --olive: #8c9e14;
    --lime: #c9cc1c;
    --amber: #d39a10;
    --rust: #b8600c;
    --red: #e0200c;
    --deep-red: #a80c08;
    --orange: #f27a0a;
    --green: #35c21c;
    --dark-green: #1d8a10;
    --navy: #14146e;
    --cream: #fbe9a4;
    --white: #ffffff;
    --chip: #d9b469;
  }
  html, body {
    margin: 0;
    padding: 0;
    width: 847px;
    height: 1200px;
    overflow: hidden;
    background: #ffffff;
  }
  .pouch {
    display: block;
    width: 847px;
    height: 1200px;
  }
  .brand-name {
    font-family: "Lilita One", sans-serif;
    font-size: 62px;
    fill: var(--cream);
  }
  .product-type {
    font-family: "Audiowide", sans-serif;
    font-size: 78px;
    fill: var(--white);
    letter-spacing: 2px;
  }
  .net-weight {
    font-family: "Roboto", sans-serif;
    font-weight: 500;
    font-size: 20px;
    fill: var(--white);
  }
</style>
</head>
<body>
<svg class="pouch" viewBox="0 0 638 904" xmlns="http://www.w3.org/2000/svg" aria-label="ZapZop crisp pouch front">
  <defs>
    <linearGradient id="bg-sweep" x1="0" y1="0" x2="1" y2="1">
      <stop offset="0" stop-color="var(--olive)"/>
      <stop offset="0.45" stop-color="var(--lime)"/>
      <stop offset="0.75" stop-color="var(--amber)"/>
      <stop offset="1" stop-color="var(--rust)"/>
    </linearGradient>
    <linearGradient id="red-band" x1="0" y1="0" x2="1" y2="0">
      <stop offset="0" stop-color="var(--red)"/>
      <stop offset="0.6" stop-color="var(--deep-red)"/>
      <stop offset="1" stop-color="var(--red)"/>
    </linearGradient>
    <linearGradient id="top-band" x1="0" y1="0" x2="1" y2="0">
      <stop offset="0" stop-color="var(--orange)"/>
      <stop offset="0.5" stop-color="var(--red)"/>
      <stop offset="1" stop-color="var(--deep-red)"/>
    </linearGradient>
    <linearGradient id="green-base" x1="0" y1="0" x2="1" y2="0">
      <stop offset="0" stop-color="var(--dark-green)"/>
      <stop offset="0.5" stop-color="var(--green)"/>
      <stop offset="1" stop-color="var(--lime)"/>
    </linearGradient>
    <linearGradient id="frame-fill" x1="0" y1="0" x2="1" y2="1">
      <stop offset="0" stop-color="var(--orange)"/>
      <stop offset="0.5" stop-color="var(--red)"/>
      <stop offset="1" stop-color="var(--rust)"/>
    </linearGradient>
    <radialGradient id="shield-fill" cx="0.5" cy="0.45" r="0.6">
      <stop offset="0" stop-color="#6ee83a"/>
      <stop offset="1" stop-color="var(--dark-green)"/>
    </radialGradient>
    <radialGradient id="chip-fill" cx="0.5" cy="0.5" r="0.6">
      <stop offset="0" stop-color="#f0d58c"/>
      <stop offset="1" stop-color="var(--chip)"/>
    </radialGradient>
  </defs>

  <!-- background -->
  <rect class="backdrop" width="638" height="904" fill="url(#bg-sweep)"/>

  <!-- top right bands -->
  <g class="top-bands">
    <polygon points="150,0 638,0 638,215" fill="url(#top-band)"/>
    <polygon points="250,0 638,0 638,110" fill="var(--deep-red)"/>
    <polygon points="190,0 230,0 638,190 638,205" fill="var(--orange)"/>
  </g>

  <!-- bottom bands -->
  <g class="bottom-bands">
    <polygon points="0,505 638,760 638,860 0,780" fill="url(#red-band)"/>
    <polygon points="0,548 638,790 638,800 0,566" fill="var(--orange)"/>
    <polygon points="0,610 638,820 638,835 0,640" fill="var(--red)" opacity="0.6"/>
    <polygon points="0,770 638,860 638,904 0,904" fill="url(#green-base)"/>
    <polygon points="380,904 638,840 638,904" fill="var(--lime)"/>
    <polygon points="430,904 638,870 638,904" fill="var(--orange)"/>
  </g>

  <!-- product photo area -->
  <g class="product-photo" role="img" aria-label="Heap of ridged seasoned potato crisps">
    <path d="M125,215 C140,170 190,150 200,120 C215,80 260,58 320,60 C380,62 420,90 430,130 C480,150 520,180 525,215 L525,300 L125,300 Z" fill="url(#chip-fill)"/>
  </g>

  <!-- chevron shield -->
  <g class="shield">
    <polygon points="96,205 320,325 552,205 560,520 320,612 80,520" fill="url(#frame-fill)"/>
    <polygon points="108,228 320,340 540,228 540,505 320,590 100,505" fill="var(--amber)" opacity="0.7"/>
    <polygon points="118,238 320,345 528,238 528,498 320,578 112,498" fill="url(#shield-fill)"/>
    <polygon points="132,248 320,348 516,248 516,488 320,566 124,488" fill="none" stroke="var(--navy)" stroke-width="3"/>
  </g>

  <!-- brand name -->
  <text class="brand-name" x="320" y="432" text-anchor="middle">ZapZop</text>

  <!-- product type -->
  <text class="product-type" x="292" y="785" text-anchor="middle" transform="rotate(4 292 760)">CRISP</text>

  <!-- net weight tab -->
  <g class="weight-tab">
    <polygon points="33,836 112,830 112,868 33,872" fill="var(--navy)"/>
    <text class="net-weight" x="72" y="859" text-anchor="middle">180g</text>
  </g>
</svg>
</body>
</html>
```